Corvale Holdings Business Cards

Hello. I need business cards designed with our new logo. I'd like to see at least 3 different designs. At least one with a dark background, and at least one with a white background. Maybe one with gray or blue for the background. Play with gradient colors and maybe even insert a pic of a skyline in the background of one or more of them. Use your judgement. We will need 2 cards printed. They need to accommodate the employee name, title, company address, phone, email, and website. Thanks.

Target Market(s)

Wealthy mature investors.

Contact Information for Business Card

Single-sided, professional, clean design that incorporates our logo.

Font styles to use
Sans Serif

Requirements
Must have
• Our new logo needs to be featured on it. (See attached.)
• Employee Name (In all CAPS)
• Title
• Street Address, City, ST Zip Code
• Cell Phone #, Email Address, Website Address
Nice to have
• Design that blends well with our new logo and its colors, or a city scape or other graphic design that looks like an apartment complex in the background. Blues and grays are nice, but use your judgement.
Should not have
• Modern or oriental looking designs or bright colors.

```html
<!DOCTYPE html>
<html lang="en">
<head>
<meta charset="utf-8">
<title>Corvale Holdings Business Cards</title>
<link rel="stylesheet" href="https://fonts.googleapis.com/css2?family=Montserrat:wght@400;500;600;700&display=swap">
<style>
  :root {
    --backdrop: #1b1c1f;
    --card: #26292c;
    --card-edge: #2e3235;
    --blue: #2a9fd8;
    --gray-text: #8d9094;
    --light-text: #b7babd;
    --skyline-top: #3a3d40;
    --skyline-bottom: #4a4d50;
  }
  * { box-sizing: border-box; margin: 0; padding: 0; }
  html, body { width: 1200px; height: 800px; overflow: hidden; }
  body {
    background: var(--backdrop);
    font-family: "Montserrat", sans-serif;
    position: relative;
  }
  .card {
    position: absolute;
    top: 248px;
    width: 530px;
    height: 303px;
    background: var(--card);
    border: 1px solid var(--card-edge);
    overflow: hidden;
  }
  .card--front { left: 50px; }
  .card--back { left: 620px; }

  .wordmark {
    position: absolute;
    display: flex;
    align-items: center;
    gap: 12px;
  }
  .wordmark__square {
    width: 30px; height: 30px;
    background: var(--blue);
  }
  .wordmark__name {
    font-weight: 700;
    color: var(--blue);
    font-size: 30px;
    letter-spacing: 1.5px;
    line-height: 1;
  }
  .wordmark__sub {
    font-weight: 700;
    color: var(--blue);
    font-size: 12.5px;
    letter-spacing: 2.4px;
    margin-top: 5px;
  }
  .card--front .wordmark { left: 110px; top: 82px; }

  .skyline {
    position: absolute;
    left: 0; right: 0; bottom: 0;
    height: 118px;
    background: linear-gradient(180deg, var(--skyline-top), var(--skyline-bottom));
    opacity: .55;
  }

  .card--back .wordmark { left: 34px; top: 48px; }
  .card--back .wordmark__name { font-size: 26px; }
  .card--back .wordmark__sub { font-size: 11px; letter-spacing: 2px; }

  .person {
    position: absolute;
    left: 34px; top: 160px;
  }
  .person__name {
    font-weight: 700;
    font-size: 15px;
    color: var(--gray-text);
    letter-spacing: .5px;
  }
  .person__title {
    font-weight: 500;
    font-size: 12px;
    color: var(--blue);
    margin-top: 2px;
  }
  .rule {
    position: absolute;
    left: 150px; right: 34px; top: 178px;
    height: 1.5px;
    background: var(--blue);
  }
  .contacts {
    position: absolute;
    left: 34px; top: 210px;
    list-style: none;
    font-size: 11.5px;
    color: var(--light-text);
  }
  .contacts li {
    display: flex; align-items: center; gap: 9px;
    margin-bottom: 7px;
  }
  .contacts svg { width: 12px; height: 12px; flex: none; }
  .contacts .accent { color: var(--blue); }
  .address {
    position: absolute;
    right: 34px; top: 120px;
    text-align: right;
    font-size: 11px;
    line-height: 1.5;
    color: var(--gray-text);
  }
</style>
</head>
<body>

<section class="card card--front" aria-label="Business card front">
  <div class="wordmark">
    <span class="wordmark__square"></span>
    <div>
      <div class="wordmark__name">CORVALE</div>
      <div class="wordmark__sub">HOLDINGS, LLC</div>
    </div>
  </div>
  <div class="skyline" role="img" aria-label="Gray city skyline silhouette along the bottom of the card"></div>
</section>

<section class="card card--back" aria-label="Business card back">
  <div class="wordmark">
    <span class="wordmark__square"></span>
    <div>
      <div class="wordmark__name">CORVALE</div>
      <div class="wordmark__sub">HOLDINGS, LLC</div>
    </div>
  </div>

  <address class="address">
    PO BOX 418 Arden Road<br>27th street Melbourne
  </address>

  <div class="person">
    <div class="person__name">MARTIN HALE</div>
    <div class="person__title">Founder</div>
  </div>
  <div class="rule"></div>

  <ul class="contacts">
    <li>
      <svg viewBox="0 0 12 12" aria-hidden="true"><rect x="2" y="1" width="8" height="10" rx="1.5" fill="none" stroke="#b7babd" stroke-width="1.3"/><circle cx="6" cy="9" r=".8" fill="#b7babd"/></svg>
      (555) 214-3380
    </li>
    <li>
      <svg viewBox="0 0 12 12" aria-hidden="true"><rect x="1" y="2.5" width="10" height="7" fill="#b7babd"/><path d="M1 2.5 6 6.5 11 2.5" fill="none" stroke="#26292c" stroke-width="1"/></svg>
      info@corvaleholdings.com
    </li>
    <li>
      <svg viewBox="0 0 12 12" aria-hidden="true"><circle cx="6" cy="6" r="5" fill="none" stroke="#b7babd" stroke-width="1.1"/><ellipse cx="6" cy="6" rx="2.2" ry="5" fill="none" stroke="#b7babd" stroke-width="1"/><path d="M1 6h10" stroke="#b7babd" stroke-width="1"/></svg>
      <span>www.<span class="accent">corvaleholdings</span>.com</span>
    </li>
  </ul>
</section>

</body>
</html>
```